Innovative Alcoholic Beverage Can Design - Part Two

Hello how are you?
You made two packaging designs for my product, “velmora cocktail”. However, you designed only one of the drink's flavors, the "Nokra Vale".
Now, I would like you to design the packaging for the other three flavors: “Brisel”; "Lunet Drift" and "Zamiro".
Guidelines:
In the designs of the three flavors, the words "velmora" and "cocktail", must be written with the same fonts that were used in the winning design of the previous project (the black can). The fonts must be the same size used in the previous project. You will choose the font color.
The information “269 mL” and “8% alc / vol” must also follow the same pattern (except color) from the previous project.
Regarding the flavors: “Brisel” is a pale yellow drink; "Lunet Drift" has a purple color and "Zamiro" is green.
Don't use the rose again. It will be exclusive to the nokra vale flavor.
I want the same impact caused by the previous project: that the public see the can and say “wow”!

```html
<!DOCTYPE html>
<html lang="en">
<head>
<meta charset="utf-8">
<title>velmora cocktail – Lunet Drift</title>
<link rel="stylesheet" href="https://fonts.googleapis.com/css2?family=UnifrakturCook:wght@700&family=Almendra:wght@400&family=Cinzel:wght@400&display=swap">
<style>
  :root {
    --can-black: #000000;
    --flavor-violet: #4414ff;
    --splash-violet: #6a4cf0;
    --label-grey: #8a8a8a;
  }
  html, body {
    margin: 0;
    padding: 0;
    width: 843px;
    height: 1200px;
    overflow: hidden;
    background: var(--can-black);
  }
  .label {
    display: block;
    width: 843px;
    height: 1200px;
  }
  .brand-name {
    font-family: "UnifrakturCook", serif;
    font-weight: 700;
    font-size: 250px;
    fill: var(--flavor-violet);
  }
  .product-type {
    font-family: "Almendra", serif;
    font-size: 108px;
    fill: var(--label-grey);
  }
  .flavor-name {
    font-family: "Almendra", serif;
    font-size: 150px;
    fill: var(--flavor-violet);
  }
  .can-info {
    font-family: "Cinzel", serif;
    font-size: 31px;
    letter-spacing: 1px;
    fill: var(--label-grey);
  }
</style>
</head>
<body>
<svg class="label" viewBox="0 0 843 1200" xmlns="http://www.w3.org/2000/svg">
  <defs>
    <radialGradient id="splash-tone" cx="50%" cy="50%" r="50%">
      <stop offset="0%" stop-color="#000000"/>
      <stop offset="55%" stop-color="#2a1a70"/>
      <stop offset="80%" stop-color="#6a4cf0" stop-opacity="0.85"/>
      <stop offset="100%" stop-color="#000000" stop-opacity="0"/>
    </radialGradient>
  </defs>

  <rect class="can-background" width="843" height="1200" fill="var(--can-black)"/>

  <text class="brand-name" x="421" y="258" text-anchor="middle">velmora</text>
  <text class="product-type" x="782" y="350" text-anchor="end">Cocktail</text>

  <rect class="flavor-splash" x="136" y="330" width="594" height="592"
        fill="url(#splash-tone)" role="img"
        aria-label="Illustration of a swirling purple liquid splash with droplets and thin light rays"/>

  <text class="flavor-name" x="405" y="1030" text-anchor="middle">Lunet Drift</text>

  <text class="can-info volume" x="168" y="1163">269 ML</text>
  <text class="can-info strength" x="405" y="1163">8% ALC/VOL</text>
</svg>
</body>
</html>
```